School Hallway Magnetic Display Design for school values

I am looking for a someone to help me design a magnetic hallway display that will hang in the hallway of our small school. There are several elements, including 1. 6ft by 4ft designed magnetic bulletin board, 2. Magnets that will stick to the board. See attachment for which elements belong where. The display will be for our TRAVEK program, which rewards students for demonstrating our school values. We want the display to be beautiful and interactive. We are also rebranding, so we want the design to align with our new fonts and colors. In the attached PDF is an outline of our new brand guidelines. Unfortunately, we don't have the color codes, but I'm hoping that you can match the colors listed. Attached are elements to be used on the board, but please use your creativity to make it more dynamic and visually appealing. For example, the star magnets could be another shape. The TRAVEK magnets must remain the same. I've included two photos of boards at other schools that inspired this project.

Target Market(s)

School Community

Industry/Entity Type

Education

Requirements
Should not have
• School Logo

```html
<!DOCTYPE html>
<html lang="en">
<head>
<meta charset="utf-8">
<title>Travek of the Month – Hallway Magnetic Board</title>
<link rel="stylesheet" href="https://fonts.googleapis.com/css2?family=Montserrat:wght@600;700;800&display=swap">
<style>
  :root {
    --green: #1f8a4c;
    --green-dark: #17703c;
    --gold: #e8b23a;
    --gold-soft: #f4d48a;
    --blue-soft: #a9c4e8;
    --green-soft: #a8d3b0;
    --ink: #222;
    --paper: #ffffff;
  }
  html, body {
    margin: 0;
    width: 1200px;
    height: 1200px;
    overflow: hidden;
    background: var(--paper);
    font-family: "Montserrat", Arial, sans-serif;
  }
  .canvas { display: block; width: 1200px; height: 1200px; }
  .dimension-line { stroke: #444; stroke-width: 1.4; fill: none; }
  .dimension-label { font-family: "Montserrat", Arial, sans-serif; font-size: 20px; font-weight: 600; fill: var(--ink); }
  .dimension-label--small { font-size: 16px; }
  .board-title { font-family: "Montserrat", Arial, sans-serif; font-weight: 800; font-size: 58px; }
  .board-title__lead { fill: var(--green); }
  .board-title__rest { fill: var(--gold); }
  .value-tag__frame { fill: var(--paper); stroke: var(--green); stroke-width: 6; }
  .value-tag__label { font-family: "Montserrat", Arial, sans-serif; font-weight: 700; font-size: 35px; fill: var(--green); }
  .thermo-label { font-family: "Montserrat", Arial, sans-serif; font-weight: 700; font-size: 20px; fill: var(--green); }
  .thermo-tick { stroke: var(--green); stroke-width: 4; }
</style>
</head>
<body>
<svg class="canvas" viewBox="0 0 1200 1200" xmlns="http://www.w3.org/2000/svg">
  <defs>
    <linearGradient id="corner-tones" x1="0" y1="0" x2="1" y2="1">
      <stop offset="0" stop-color="#f4d48a"/>
      <stop offset="0.5" stop-color="#a8d3b0"/>
      <stop offset="1" stop-color="#a9c4e8"/>
    </linearGradient>
    <linearGradient id="tag-cap" x1="0" y1="0" x2="1" y2="1">
      <stop offset="0" stop-color="#a9c4e8"/>
      <stop offset="0.5" stop-color="#f4d48a"/>
      <stop offset="1" stop-color="#e8b23a"/>
    </linearGradient>
    <linearGradient id="thermo-fill" x1="0" y1="0" x2="0" y2="1">
      <stop offset="0" stop-color="#ffffff"/>
      <stop offset="0.45" stop-color="#f4d48a"/>
      <stop offset="1" stop-color="#e8b23a"/>
    </linearGradient>
    <clipPath id="board-clip"><rect x="88" y="250" width="1023" height="713"/></clipPath>
  </defs>

  <!-- dimension annotations -->
  <g class="dimensions">
    <line class="dimension-line" x1="88" y1="229" x2="1111" y2="229"/>
    <line class="dimension-line" x1="88" y1="221" x2="88" y2="237"/>
    <line class="dimension-line" x1="1111" y1="221" x2="1111" y2="237"/>
    <text class="dimension-label" x="599" y="218" text-anchor="middle">72″</text>
    <line class="dimension-line" x1="1131" y1="250" x2="1131" y2="963"/>
    <line class="dimension-line" x1="1123" y1="250" x2="1139" y2="250"/>
    <line class="dimension-line" x1="1123" y1="963" x2="1139" y2="963"/>
    <text class="dimension-label" x="1157" y="613" text-anchor="middle">48″</text>
  </g>

  <!-- board -->
  <g class="board">
    <rect x="88" y="250" width="1023" height="713" fill="#fff"/>
    <g clip-path="url(#board-clip)">
      <polygon role="img" aria-label="Geometric facet pattern, top left corner" points="88,250 300,250 230,340 88,430" fill="url(#corner-tones)" opacity="0.55"/>
      <polygon role="img" aria-label="Geometric facet pattern, top right corner" points="880,250 1111,250 1111,420 1000,330" fill="url(#corner-tones)" opacity="0.55"/>
      <polygon role="img" aria-label="Geometric facet pattern, bottom left corner" points="88,620 200,700 380,780 480,963 88,963" fill="url(#corner-tones)" opacity="0.55"/>
      <polygon role="img" aria-label="Geometric facet pattern, bottom right corner" points="1111,800 1111,963 960,963" fill="url(#corner-tones)" opacity="0.55"/>
    </g>
    <rect x="92" y="254" width="1015" height="705" fill="none" stroke="var(--green)" stroke-width="8"/>

    <text class="board-title" x="598" y="340" text-anchor="middle"><tspan class="board-title__lead">Travek</tspan><tspan class="board-title__rest"> of the Month</tspan></text>

    <!-- tag size annotation -->
    <line class="dimension-line" x1="162" y1="404" x2="471" y2="404"/>
    <line class="dimension-line" x1="162" y1="398" x2="162" y2="410"/>
    <line class="dimension-line" x1="471" y1="398" x2="471" y2="410"/>
    <text class="dimension-label dimension-label--small" x="316" y="396" text-anchor="middle">21″</text>
    <line class="dimension-line" x1="146" y1="422" x2="146" y2="504"/>
    <line class="dimension-line" x1="140" y1="422" x2="152" y2="422"/>
    <line class="dimension-line" x1="140" y1="504" x2="152" y2="504"/>
    <text class="dimension-label dimension-label--small" x="130" y="469" text-anchor="middle">6″</text>

    <!-- value tags -->
    <g class="value-tag">
      <rect class="value-tag__frame" x="162" y="422" width="309" height="82" rx="9"/>
      <rect role="img" aria-label="Facet accent" x="168" y="428" width="22" height="70" fill="url(#tag-cap)" opacity="0.7"/>
      <rect role="img" aria-label="Facet accent" x="443" y="428" width="22" height="70" fill="url(#tag-cap)" opacity="0.7"/>
      <text class="value-tag__label" x="316" y="475" text-anchor="middle">Simplicity</text>
    </g>
    <g class="value-tag">
      <rect class="value-tag__frame" x="504" y="422" width="307" height="82" rx="9"/>
      <rect role="img" aria-label="Facet accent" x="510" y="428" width="22" height="70" fill="url(#tag-cap)" opacity="0.7"/>
      <rect role="img" aria-label="Handshake icon" x="745" y="443" width="40" height="38" rx="6" fill="var(--gold-soft)"/>
      <text class="value-tag__label" x="644" y="475" text-anchor="middle">Peace</text>
    </g>
    <g class="value-tag">
      <rect class="value-tag__frame" x="162" y="543" width="309" height="82" rx="9"/>
      <rect role="img" aria-label="Facet accent" x="168" y="549" width="22" height="70" fill="url(#tag-cap)" opacity="0.7"/>
      <rect role="img" aria-label="Facet accent" x="443" y="549" width="22" height="70" fill="url(#tag-cap)" opacity="0.7"/>
      <text class="value-tag__label" x="316" y="596" text-anchor="middle">Integrity</text>
    </g>
    <g class="value-tag">
      <rect class="value-tag__frame" x="504" y="543" width="307" height="82" rx="9"/>
      <rect role="img" aria-label="People icon" x="508" y="564" width="32" height="38" rx="6" fill="var(--blue-soft)"/>
      <rect role="img" aria-label="People icon" x="768" y="564" width="32" height="38" rx="6" fill="var(--blue-soft)"/>
      <text class="value-tag__label" x="654" y="596" text-anchor="middle">Community</text>
    </g>
    <g class="value-tag">
      <rect class="value-tag__frame" x="162" y="650" width="309" height="82" rx="9"/>
      <rect role="img" aria-label="Facet accent" x="168" y="656" width="22" height="70" fill="url(#tag-cap)" opacity="0.7"/>
      <rect role="img" aria-label="Facet accent" x="443" y="656" width="22" height="70" fill="url(#tag-cap)" opacity="0.7"/>
      <text class="value-tag__label" x="316" y="703" text-anchor="middle">Equality</text>
    </g>
    <g class="value-tag">
      <rect class="value-tag__frame" x="504" y="650" width="307" height="82" rx="9"/>
      <rect role="img" aria-label="Facet accent" x="510" y="656" width="22" height="70" fill="url(#tag-cap)" opacity="0.7"/>
      <rect role="img" aria-label="Leaf icon" x="766" y="672" width="24" height="38" rx="12" fill="var(--green-soft)"/>
      <text class="value-tag__label" x="640" y="703" text-anchor="middle">Stewardship</text>
    </g>

    <!-- reward magnets -->
    <g class="reward-magnets">
      <line x1="480" y1="826" x2="920" y2="826" stroke="var(--gold)" stroke-width="6"/>
      <circle cx="482" cy="830" r="36" fill="var(--green)" stroke="#cfe3f5" stroke-width="5"/>
      <circle cx="566" cy="815" r="32" fill="var(--gold-soft)" stroke="var(--green)" stroke-width="4"/>
      <circle cx="651" cy="815" r="32" fill="var(--blue-soft)" stroke="var(--gold)" stroke-width="4"/>
      <circle cx="738" cy="820" r="30" fill="var(--green)" stroke="var(--gold)" stroke-width="4"/>
      <circle cx="535" cy="898" r="32" fill="#fff" stroke="var(--green-soft)" stroke-width="4"/>
      <circle cx="614" cy="885" r="30" fill="var(--blue-soft)" stroke="var(--green)" stroke-width="4"/>
      <circle cx="677" cy="898" r="32" fill="var(--gold)" stroke="var(--green)" stroke-width="4"/>
      <circle cx="752" cy="898" r="28" fill="var(--blue-soft)" stroke="var(--green)" stroke-width="4"/>
    </g>

    <!-- progress thermometer -->
    <g class="thermometer">
      <rect x="865" y="384" width="110" height="440" rx="55" fill="var(--green)"/>
      <circle cx="920" cy="826" r="92" fill="var(--green)"/>
      <rect x="872" y="391" width="96" height="433" rx="48" fill="#fff"/>
      <circle cx="920" cy="826" r="85" fill="#fff"/>
      <rect x="879" y="398" width="82" height="426" rx="41" fill="var(--gold)"/>
      <circle cx="920" cy="826" r="78" fill="var(--gold)"/>
      <rect x="885" y="404" width="70" height="420" rx="35" fill="var(--green)"/>
      <circle cx="920" cy="826" r="72" fill="var(--green)"/>
      <rect x="891" y="410" width="58" height="414" rx="29" fill="#fff"/>
      <circle cx="920" cy="826" r="66" fill="#fff"/>
      <rect x="900" y="530" width="40" height="300" rx="20" fill="url(#thermo-fill)"/>
      <circle cx="920" cy="826" r="58" fill="var(--gold)"/>
      <g class="thermo-scale">
        <line class="thermo-tick" x1="976" y1="430" x2="1010" y2="430"/>
        <line class="thermo-tick" x1="976" y1="453" x2="994" y2="453"/>
        <line class="thermo-tick" x1="976" y1="476" x2="994" y2="476"/>
        <line class="thermo-tick" x1="976" y1="499" x2="994" y2="499"/>
        <line class="thermo-tick" x1="976" y1="522" x2="994" y2="522"/>
        <line class="thermo-tick" x1="976" y1="545" x2="994" y2="545"/>
        <line class="thermo-tick" x1="976" y1="568" x2="994" y2="568"/>
        <line class="thermo-tick" x1="976" y1="591" x2="994" y2="591"/>
        <line class="thermo-tick" x1="976" y1="614" x2="994" y2="614"/>
        <line class="thermo-tick" x1="976" y1="637" x2="994" y2="637"/>
        <line class="thermo-tick" x1="976" y1="660" x2="994" y2="660"/>
        <line class="thermo-tick" x1="976" y1="683" x2="994" y2="683"/>
        <line class="thermo-tick" x1="976" y1="706" x2="994" y2="706"/>
        <line class="thermo-tick" x1="976" y1="729" x2="994" y2="729"/>
        <line class="thermo-tick" x1="976" y1="750" x2="1010" y2="750"/>
      </g>
      <text class="thermo-label" x="1016" y="437">Goal</text>
      <text class="thermo-label" x="1016" y="757">Start</text>
    </g>
  </g>
</svg>
</body>
</html>
```